Restaurant menu design

Design fine dinning menu for Indian restaurant. Restaurant location is on river side. So if design has some touch of Yarra river of Melbourne and Indian touch. It is not compulsory. Creative and modern design is required.
I want to print in A3 and folded take away sizes so design should for both.
1. In A3, backside we need to design drink menu. I am attaching our current restaurant menu for drinks name and price.

Target Market(s)

Indian / Australian Customer

Industry/Entity Type

Indian Food, Indian fine dining

Colors
F0912C
F2A743
F7CA91
FBE8D2
FDF5EE

Requirements
Must have
• Simple but district design
Should not have
• common other restaurant type menu. Too many colours.

```html
<!DOCTYPE html>
<html lang="en">
<head>
<meta charset="utf-8">
<title>Tara's Kitchen — Menu</title>
<link href="https://fonts.googleapis.com/css2?family=Marcellus+SC&family=Alegreya:wght@400;500&display=swap" rel="stylesheet">
<style>
:root{
  --orange:#F0912C;
  --amber:#F2A743;
  --sand:#F2D386;
  --peach:#F7CA91;
  --cream:#FDF5EE;
  --blush:#FBE8D2;
  --bronze:#9A8459;
  --text:#9A7D4F;
  --desc:#8C7350;
  --white:#FFFFFF;
  --backdrop:#E7E2DB;
}
*{margin:0;padding:0;box-sizing:border-box}
html,body{width:1200px;height:800px;overflow:hidden;background:var(--backdrop)}
.menu{position:absolute;left:34px;top:0;width:1131px;height:800px;background:var(--cream);overflow:hidden;font-family:'Alegreya',Georgia,serif;color:var(--desc);line-height:1}
.panel{position:absolute;top:0;width:377px;height:800px}
.panel--left{left:0}
.panel--mid{left:377px}
.panel--right{left:754px}
.abs{position:absolute}
.sc{font-family:'Marcellus SC',Georgia,serif;color:var(--text);font-weight:400}
.photo{position:absolute;border-radius:50%}

/* lists */
.item{display:flex;justify-content:space-between;align-items:baseline}
.item__name{font-family:'Marcellus SC',Georgia,serif;color:var(--text);font-size:10.5px;line-height:11px;letter-spacing:.2px}
.entry > .item__name{display:block}
.item__price{font-family:'Marcellus SC',Georgia,serif;color:var(--text);font-size:10.5px;line-height:11px}
.item__desc{font-size:5.6px;line-height:7.7px;color:var(--desc)}
.entry{margin-bottom:5.5px}

/* left */
.title-bar{left:0;top:20px;width:322px;height:30px;background:var(--orange);color:var(--white);font-family:'Marcellus SC',Georgia,serif;font-size:21px;line-height:30px;padding-left:36px}
.tagline{left:35px;top:55px;font-size:11.5px;line-height:14.5px}
.veg-box{left:22px;top:86px;width:270px;height:193px;background:var(--white)}
.section-label{font-family:'Marcellus SC',Georgia,serif;color:var(--text);font-size:10px;line-height:12px}
.veg-list{left:35px;top:91px;width:245px}
.veg-list .section-label{margin-bottom:6px}
.strip-orange{left:326px;top:89px;width:30px;height:193px;background:var(--orange)}
.strip-sand{left:24px;top:288px;width:65px;height:214px;background:var(--sand)}
.nonveg-list{left:101px;top:286px;width:264px}
.nonveg-list .section-label{margin-bottom:9px}
.chaat{left:20px;top:511px;width:210px}
.heading-lg{font-family:'Marcellus SC',Georgia,serif;color:var(--text);font-size:17px;line-height:18px}
.chaat .item__desc{font-size:6.2px;line-height:8.6px}
.chaat .entry{margin-bottom:3px}
.indo-block{left:32px;top:637px;width:84px;height:144px;background:var(--orange)}
.indo{left:131px;top:632px;width:190px}
.indo .item__desc{font-size:6.2px;line-height:8.6px}
.indo .entry{margin-bottom:3.5px}
.indo .heading-lg{margin-bottom:1px}

/* middle */
.tab{background:var(--bronze);color:var(--cream);font-family:'Marcellus SC',Georgia,serif}
.curries-tab{left:426px;top:30px;width:140px;height:21px;font-size:12px;line-height:23px;padding-left:15px}
.curries-box{left:426px;top:51px;width:288px;height:219px;background:#FBF0E2}
.curries{left:441px;top:58px;width:248px}
.curries .entry{margin-bottom:8.5px}
.special-bar{left:426px;top:277px;width:282px;height:17px;background:var(--orange);color:var(--white);font-family:'Marcellus SC',Georgia,serif;font-size:10px;line-height:18px;padding-left:15px}
.special-col{left:647px;top:294px;width:45px;height:278px;background:var(--sand)}
.special{left:441px;top:300px;width:248px}
.special .item__desc{font-size:6px;line-height:8.4px}
.special .entry{margin-bottom:6.6px}
.special .item__price{width:45px;text-align:center;margin-right:3px}
.mains-box{left:426px;top:584px;width:282px;height:179px;background:var(--bronze)}
.mains{left:443px;top:592px;width:255px}
.mains .section-label,.mains .item__name,.mains .item__price{color:var(--cream)}
.mains .section-label{font-size:11px;margin-bottom:8px}
.mains .item__desc{color:var(--cream);font-size:6.2px;line-height:8.8px}
.mains .entry{margin-bottom:5px}

/* right */
.brand{left:774px;top:38px;width:350px;text-align:center;font-family:'Marcellus SC',Georgia,serif;color:var(--bronze);font-size:40px;line-height:60px}
.brand-rule{left:842px;top:36px;width:214px;height:1.5px;background:var(--orange)}
.brand-rule--low{top:104px}
.rice-box{left:774px;top:129px;width:259px;height:354px;background:var(--sand)}
.rice{left:797px;top:133px;width:288px}
.rice .heading-lg{font-size:19px;line-height:22px;margin-bottom:5px}
.rice .item__name,.rice .item__price{font-size:12.5px;line-height:14px}
.rice .item__desc{font-size:7.6px;line-height:10px;max-width:210px}
.rice .entry{margin-bottom:10.5px}
.extras-box{left:774px;top:483px;width:340px;height:147px;background:var(--white)}
.breads{left:784px;top:489px;width:158px}
.sides{left:947px;top:489px;width:147px}
.extras-head{font-family:'Marcellus SC',Georgia,serif;color:var(--text);font-size:13px;line-height:15px;margin-bottom:3px}
.breads .item__name{font-size:9.2px;line-height:10px}
.breads .item__desc{font-size:4.8px;line-height:7px}
.breads .entry{margin-bottom:6px}
.sides .item__name,.sides .item__price{font-size:7.4px;line-height:8.5px}
.sides .item__desc{font-size:3.8px;line-height:6px}
.sides .entry{margin-bottom:3.5px}
.qty{display:block;font-size:3.6px;line-height:4px;text-align:right}
.desserts-tab{left:779px;top:631px;width:129px;height:27px;font-size:18px;line-height:29px;padding-left:17px}
.desserts{left:796px;top:666px;width:286px}
.desserts .item__name,.desserts .item__price{font-size:12px;line-height:13px}
.desserts .item__desc{font-size:7.4px;line-height:10px}
.desserts .entry{margin-bottom:10px}
</style>
</head>
<body>
<main class="menu">

  <!-- LEFT PANEL -->
  <section class="panel panel--left">
    <div class="abs title-bar">Tara's Kitchen — Menu</div>
    <p class="abs tagline sc">Modern &amp; Classic Indian Dining<br>Riverside Quay, Melbourne</p>

    <div class="abs veg-box"></div>
    <div class="abs veg-list">
      <h3 class="section-label">Vegetarian Entrées</h3>
      <div class="entry"><div class="item"><span class="item__name">Classic Samosa</span><span class="item__price">$16</span></div>
        <p class="item__desc">Handcrafted pastry parcels filled with spiced potatoes &amp;<br>peas,served with a duo of fresh mint-coriander chutney<br>and sweet mango relish.</p></div>
      <div class="entry"><div class="item"><span class="item__name">Crispy Onion &amp; Spinach Bhaji</span><span class="item__price">$16</span></div>
        <p class="item__desc">Crisp golden fritters of baby spinach &amp; onion, delicately<br>spiced, paired with house chutneys.</p></div>
      <div class="entry"><div class="item"><span class="item__name">Harabhara Edamame Kebab</span><span class="item__price">$18</span></div>
        <p class="item__desc">Pan-seared medallions of edamame and garden vegetables,<br>stuffed with soft cheese and herbs, served with tangy yogurt dip.</p></div>
      <div class="entry"><div class="item"><span class="item__name">Zafrani Paneer Tikka</span><span class="item__price">$22</span></div>
        <p class="item__desc">Cubes of cottage cheese marinated in saffron, cardamom &amp; smoky<br>tandoor spices, grilled to perfection, served with mint chutney and microgreens.</p></div>
      <div class="entry"><div class="item"><span class="item__name">Vada Pav Sliders</span><span class="item__price">$16</span></div>
        <p class="item__desc">A gourmet take on Mumbai's street legend: spiced potato croquette<br>in a butter brioche bun, layered with tamarind, mint-coriander chutney<br>&amp; fiery thecha, accompanied by crisp fried green chilli.</p></div>
    </div>
    <div class="abs strip-orange"></div>
    <div class="photo" role="img" aria-label="Photo of golden samosas with dipping sauce on lettuce" style="left:287px;top:142px;width:82px;height:82px;background:radial-gradient(circle at 45% 45%,#E2B25C,#A8823A 55%,#3E4A24 80%,#2A2A26)"></div>

    <div class="abs strip-sand"></div>
    <div class="photo" role="img" aria-label="Photo of tandoori chicken pieces on a plate" style="left:6px;top:375px;width:92px;height:64px;background:radial-gradient(ellipse at 50% 50%,#B8532A,#D07A45 50%,#EFE3D2 75%,#F6EEE4)"></div>
    <div class="abs nonveg-list">
      <h3 class="section-label">Non-Vegetarian Entrées</h3>
      <div class="entry"><div class="item"><span class="item__name">Smoke Tandoori Chicken Tikka</span><span class="item__price">$20</span></div>
        <p class="item__desc">Charcoal-grilled chicken marinated overnight with aromatic<br>spices, finished with a touch of smokey infusion.</p></div>
      <div class="entry"><div class="item"><span class="item__name">Chicken Malai Tikka</span><span class="item__price">$20</span></div>
        <p class="item__desc">Tender chicken morsels marinated in cream, cheese &amp; cardamom,<br>cooked gently in the tandoor for a melt-in-mouth experience.</p></div>
      <div class="entry"><div class="item"><span class="item__name">Awadhi Fish Tikka</span><span class="item__price">$22</span></div>
        <p class="item__desc">Fresh barramundi fillets marinated with hand-pounded<br>Awadhi spices, grilled for a delicate smokey finish.</p></div>
      <div class="entry"><div class="item"><span class="item__name">Tandoori Tiger Prawns</span><span class="item__price">$24</span></div>
        <p class="item__desc">Jumbo prawns infused with curry-leaf butter, garlic &amp; chilli,<br>char-grilled for an indulgent coastal flavour.</p></div>
      <div class="entry"><div class="item"><span class="item__name">Lamb Gilafi Seekh</span><span class="item__price">$22</span></div>
        <p class="item__desc">Minced lamb spiced with herbs, peppers &amp; aromatics, skewered &amp;<br>flame-roasted, served with minted yogurt.</p></div>
      <div class="entry"><div class="item"><span class="item__name">Tandoori Platter</span><span class="item__price">$39</span></div>
        <p class="item__desc">A chef's selection of smoky tandoori classics: Chicken Tikka,<br>Malai Tikka, Lamb Seekh &amp; Awadhi Fish, presented with a medley<br>of chutneys &amp; dips.</p></div>
    </div>

    <div class="abs chaat">
      <h2 class="heading-lg">Chaat</h2>
      <div class="entry"><div class="item"><span class="item__name">Panipuri Experience</span><span class="item__price">$20</span></div>
        <p class="item__desc">Crisp puris filled with spiced potato, tangy chutneys &amp; chilled<br>spiced water — a refined version of the street favourite.</p></div>
      <div class="entry"><div class="item"><span class="item__name">Burrata Chaat</span><span class="item__price">$20</span></div>
        <p class="item__desc">Creamy burrata resting on crispy papdi, layered with tamarind<br>glaze, mint chutney &amp; golden sev.</p></div>
      <div class="entry"><div class="item"><span class="item__name">Deconstructed Samosa Chaat</span><span class="item__price">$18</span></div>
        <p class="item__desc">Crispy samosa pastry crumbles over spiced potato &amp; peas,<br>dressed with chutneys, yogurt &amp; pomegranate jewels.</p></div>
    </div>

    <div class="abs indo-block"></div>
    <div class="photo" role="img" aria-label="Photo of a white bowl of stir-fried noodles with vegetables" style="left:20px;top:670px;width:102px;height:70px;background:radial-gradient(ellipse at 50% 45%,#C9873E,#A45A2C 45%,#F4EFE8 68%,#FFFFFF)"></div>
    <div class="abs indo">
      <h2 class="heading-lg">Indo-Chinese</h2>
      <div class="entry"><div class="item"><span class="item__name">Vegetable Manchurian Dry</span><span class="item__price">$22</span></div>
        <p class="item__desc">Golden-fried vegetable dumplings wok-tossed<br>in garlic, chilli &amp; soy glaze.</p></div>
      <div class="entry"><div class="item"><span class="item__name">Paneer Chilli Dry</span><span class="item__price">$24</span></div>
        <p class="item__desc">Cottage cheese cubes tossed with peppers, onions<br>&amp; chilli-garlic soy reduction.</p></div>
      <div class="entry"><div class="item"><span class="item__name">Chilli Chicken Dry</span><span class="item__price">$26</span></div>
        <p class="item__desc">Tender chicken tossed with shallots, peppers<br>&amp; fiery Indo-Chinese sauce.</p></div>
      <div class="entry"><div class="item"><span class="item__name">Oriental Noodles —</span><span class="item__price">Veg $22</span></div>
        <div class="item"><p class="item__desc">Stir-fried noodles with seasonal vegetables,<br>wok-seared with soy &amp; garlic.</p><span class="item__price">Chicken $24</span></div></div>
    </div>
  </section>

  <!-- MIDDLE PANEL -->
  <section class="panel panel--mid"></section>
  <div class="abs tab curries-tab">Classic Curries</div>
  <div class="abs curries-box"></div>
  <div class="abs curries">
    <div class="entry"><div class="item"><span class="item__name">Paneer / Kofta / Mixed Veg</span><span class="item__price">$26</span></div><p class="item__desc">Choose your protein with a choice of gourmet curry bases.</p></div>
    <div class="entry"><div class="item"><span class="item__name">Chicken / Lamb</span><span class="item__price">$28</span></div><p class="item__desc">Choose your protein with a choice of gourmet curry bases.</p></div>
    <div class="entry"><div class="item"><span class="item__name">Prawns / Fish</span><span class="item__price">$30</span></div><p class="item__desc">Choose your protein with a choice of gourmet curry bases.</p></div>
    <div class="entry"><div class="item"><span class="item__name">Vindaloo</span></div><p class="item__desc">Fiery Goan-style curry with red chillies &amp; vinegar.</p></div>
    <div class="entry"><div class="item"><span class="item__name">Saag</span></div><p class="item__desc">Creamy buttered spinach slow-cooked with spices.</p></div>
    <div class="entry"><div class="item"><span class="item__name">Korma</span></div><p class="item__desc">Mild, creamy cashew &amp; saffron curry.</p></div>
    <div class="entry"><div class="item"><span class="item__name">Masala</span></div><p class="item__desc">Tomato &amp; onion base enriched with cream &amp; butter.</p></div>
    <div class="entry"><div class="item"><span class="item__name">Madras</span></div><p class="item__desc">Coconut-based curry with onions, garlic &amp; curry leaves.</p></div>
  </div>

  <div class="abs special-bar">Tara's Kitchen Special Vegetarian Curries</div>
  <div class="abs special-col"></div>
  <div class="photo" role="img" aria-label="Photo of a bowl of kofta curry garnished with green chilli" style="left:369px;top:292px;width:64px;height:64px;background:radial-gradient(circle at 50% 50%,#E0962E,#C8741E 50%,#2E3A44 78%,#1F2A33)"></div>
  <div class="abs special">
    <div class="entry"><div class="item"><span class="item__name">Sham Savera Kofta</span><span class="item__price">$26</span></div><p class="item__desc">Spinach dumplings filled with cottage cheese, simmered in<br>a rich tomato-butter sauce — a true royal delicacy.</p></div>
    <div class="entry"><div class="item"><span class="item__name">Mexican Salsa Paneer</span><span class="item__price">$28</span></div><p class="item__desc">Paneer cubes tossed in a fusion of roasted Mexican-style<br>tomato salsa and Indian spices — a bold East-meets-West creation.</p></div>
    <div class="entry"><div class="item"><span class="item__name">Mushroom Mutter Masala</span><span class="item__price">$28</span></div><p class="item__desc">Tender mushrooms and garden peas in a spiced onion-tomato<br>gravy, finished with cream.</p></div>
    <div class="entry"><div class="item"><span class="item__name">Kaju Curry</span><span class="item__price">$28</span></div><p class="item__desc">A luxurious cashew-based curry enriched with aromatic spices,<br>velvety texture &amp; buttery finish.</p></div>
    <div class="entry"><div class="item"><span class="item__name">Cheese Butter Masala</span><span class="item__price">$28</span></div><p class="item__desc">Paneer and soft cheese in a creamy, butter-rich tomato gravy<br>indulgent &amp; comforting.</p></div>
    <div class="entry"><div class="item"><span class="item__name">Dal Tadka —</span><span class="item__price">$22</span></div><p class="item__desc">Yellow lentils tempered with garlic, cumin &amp; chilli, offering<br>homestyle comfort with gourmet finesse.</p></div>
    <div class="entry"><div class="item"><span class="item__name">Dal Makhani</span><span class="item__price">$22</span></div><p class="item__desc">Black lentils, slow-cooked overnight with butter and cream<br>a timeless Delhi specialty.</p></div>
    <div class="entry"><div class="item"><span class="item__name">Vegetable Dum Biryani</span><span class="item__price">$28</span></div><p class="item__desc">Saffron-scented basmati rice layered with seasonal vegetables,<br>sealed and slow-cooked in the dum style, served with cooling raita.</p></div>
  </div>

  <div class="abs mains-box"></div>
  <div class="abs mains">
    <h3 class="section-label">Non-Vegetarian Mains</h3>
    <div class="entry"><div class="item"><span class="item__name">Raja Rani Chicken</span><span class="item__price">$35</span></div><p class="item__desc">Char-grilled chicken tikka wrapped in a silky egg roll, layered<br>with makhani sauce &amp; spinach gravy — regal flavours in every bite.</p></div>
    <div class="entry"><div class="item"><span class="item__name">Butter Chicken —</span><span class="item__price">$29</span></div><p class="item__desc">A refined Delhi classic: chicken simmered in a tomato<br>-butter sauce, smoky &amp; velvety.</p></div>
    <div class="entry"><div class="item"><span class="item__name">Lamb Rogan Josh</span><span class="item__price">$29</span></div><p class="item__desc">Kashmiri-style lamb curry, slow-braised in aromatic spices<br>with a deep, rich flavour.</p></div>
    <div class="entry"><div class="item"><span class="item__name">Dhaba Goat Masala</span><span class="item__price">$29</span></div><p class="item__desc">A rustic North Indian goat curry, slow-cooked with onions, garlic,<br>and earthy spices — inspired by India's iconic roadside kitchens.</p></div>
  </div>
  <div class="photo" role="img" aria-label="Photo of a bowl of spiced curry seen from above" style="left:386px;top:752px;width:82px;height:82px;background:radial-gradient(circle at 50% 50%,#B5642E,#9C4A22 55%,#F3ECE2 72%,#FFFFFF)"></div>

  <!-- RIGHT PANEL -->
  <section class="panel panel--right"></section>
  <div class="abs brand-rule"></div>
  <h1 class="abs brand">Tara's Kitchen</h1>
  <div class="abs brand-rule brand-rule--low"></div>

  <div class="abs rice-box"></div>
  <div class="abs rice">
    <h2 class="heading-lg">Rice &amp; Biryanis</h2>
    <div class="entry"><div class="item"><span class="item__name">Plain Basmati Rice</span><span class="item__price">$8</span></div><p class="item__desc">Steamed long-grain basmati rice, light &amp; fluffy.</p></div>
    <div class="entry"><div class="item"><span class="item__name">Jeera Rice</span><span class="item__price">$8</span></div><p class="item__desc">Basmati rice tempered with roasted cumin seeds.</p></div>
    <div class="entry"><div class="item"><span class="item__name">Lemon Coconut Rice</span><span class="item__price">$10</span></div><p class="item__desc">Fragrant rice infused with lemon zest, curry leaves<br>&amp; coconut.</p></div>
    <div class="entry"><div class="item"><span class="item__name">Peas Pulao</span><span class="item__price">$10</span></div><p class="item__desc">Delicate basmati rice cooked with sweet garden peas<br>&amp; whole spices.</p></div>
    <div class="entry"><div class="item"><span class="item__name">Biryani Flavoured Rice</span><span class="item__price">$15</span></div><p class="item__desc">Aromatic saffron basmati rice prepared in biryani style.</p></div>
    <div class="entry"><div class="item"><span class="item__name">Vegetable Dum Biryani —</span><span class="item__price">$28</span></div><p class="item__desc">Classic layered vegetable biryani with saffron, slow-<br>cooked dum style.</p></div>
    <div class="entry"><div class="item"><span class="item__name">Hyderabadi Chicken Biryani</span><span class="item__price">$30</span></div><p class="item__desc">Fragrant rice layered with marinated chicken, spices<br>&amp; saffron, served with raita.</p></div>
    <div class="entry"><div class="item"><span class="item__name">Lamb Dum Biryani</span><span class="item__price">$33</span></div><p class="item__desc">A celebratory lamb shank biryani, slow-cooked with<br>caramelised onions, saffron &amp; spices — rich and aromatic.</p></div>
  </div>

  <div class="abs extras-box"></div>
  <div class="abs breads">
    <h3 class="extras-head">Breads</h3>
    <div class="entry"><span class="item__name">Classic Butter Naan — $6</span><p class="item__desc">Soft, fluffy tandoor-baked bread brushed with butter.</p></div>
    <div class="entry"><span class="item__name">Garlic Naan — $7</span><p class="item__desc">Tandoor-baked naan with fresh garlic &amp; coriander.</p></div>
    <div class="entry"><span class="item__name">Lachha Paratha — $8</span><p class="item__desc">Crisp, flaky, multi-layered paratha pan-fried with ghee.</p></div>
    <div class="entry"><span class="item__name">Cheese Naan — $8</span><p class="item__desc">Stuffed with molten cheese, baked in the tandoor.</p></div>
    <div class="entry"><span class="item__name">Cheese Garlic Naan — $8.50</span><p class="item__desc">Naan layered with garlic &amp; cheese — indulgent &amp; aromatic.</p></div>
  </div>
  <div class="abs sides">
    <h3 class="extras-head">Sides</h3>
    <div class="entry"><div class="item"><span class="item__name">Cucumber Raita</span><span class="item__price">$6</span></div><p class="item__desc">Cool yogurt with cucumber, cumin &amp; mint.</p></div>
    <div class="entry"><div class="item"><span class="item__name">Roasted Papadum</span><span class="item__price">$4<span class="qty">(4 pcs)</span></span></div><p class="item__desc">Crispy lentil wafers roasted for a healthy crunch.</p></div>
    <div class="entry"><div class="item"><span class="item__name">Masala Papad</span><span class="item__price">$8<span class="qty">(2 pcs)</span></span></div><p class="item__desc">Papad topped with spiced onions, tomatoes &amp; herbs.</p></div>
    <div class="entry"><div class="item"><span class="item__name">Onion Salad</span><span class="item__price">$6</span></div><p class="item__desc">Fresh onion rings tossed with lime &amp; masala.</p></div>
    <div class="entry"><div class="item"><span class="item__name">Garden Salad</span><span class="item__price">$8</span></div><p class="item__desc">Seasonal greens dressed with lemon &amp; cumin.</p></div>
    <div class="entry"><div class="item"><span class="item__name">Mango Chutney /<br>Mint Chutney / Mixed Pickle</span><span class="item__price">$4</span></div><p class="item__desc">House-made condiments to complement your meal.</p></div>
  </div>

  <div class="abs tab desserts-tab">Desserts</div>
  <div class="abs desserts">
    <div class="entry"><div class="item"><span class="item__name">Kunafa Nest Gulab Jamun with Rabri</span><span class="item__price">$20</span></div><p class="item__desc">Golden kunafa nest cradling soft gulab jamun, draped in<br>creamy rabri &amp; pistachios.</p></div>
    <div class="entry"><div class="item"><span class="item__name">Mango Mousse Delight —</span><span class="item__price">$20</span></div><p class="item__desc">Alphonso mango mousse layered with coconut crumble &amp; fresh mint.</p></div>
    <div class="entry"><div class="item"><span class="item__name">Kulfi Falooda Trio —</span><span class="item__price">$20</span></div><p class="item__desc">Traditional kulfi in pistachio, rose &amp; saffron, served with silky falooda.</p></div>
  </div>

</main>
</body>
</html>
```